Velvette by Monica Darsh business cards

I am after a business card that will fit the name of my business - velvette.
I want something classy and sexy and nothing tacky.
Ideas that I like are Zebra print backgrounds glitter back grounds
Two ideas I had were
1. Zebra print in black and white, the name Velvette by Monica Darsh and a shilouette of a woman laying on top of the name. Or instead of zebra a glitter background.
2. Idea very similar except for instead of a woman a pair of lips maybe a hot pink glitter or a gold glitter depending on background with the business name between the lips.
Or you can do something completely different.

Industry/Entity Type

Business

```html
<!DOCTYPE html>
<html lang="en">
<head>
<meta charset="UTF-8">
<title>Velvette by Monica Darsh — Business Card</title>
<link rel="stylesheet" href="https://fonts.googleapis.com/css2?family=Poiret+One&display=swap">
<style>
  :root {
    --gold: #d4a93a;
    --gold-light: #e6c45e;
    --gold-deep: #a9801f;
    --ink: #0b0b0b;
    --panel: #ffffff;
    --type: #141414;
  }
  * { margin: 0; padding: 0; box-sizing: border-box; }
  html, body {
    width: 1200px;
    height: 686px;
    overflow: hidden;
    background: var(--panel);
  }
  .card {
    position: relative;
    width: 1200px;
    height: 686px;
    overflow: hidden;
  }
  .card__pattern {
    position: absolute;
    inset: 0;
    background:
      linear-gradient(125deg,
        var(--gold-light) 0%,
        var(--gold) 30%,
        var(--ink) 50%,
        var(--gold) 70%,
        var(--gold-deep) 100%);
  }
  .brand-panel {
    position: absolute;
    left: 251px;
    top: 145px;
    width: 700px;
    height: 395px;
    background: var(--panel);
    border-radius: 16px;
  }
  .brand-name {
    position: absolute;
    left: 0;
    right: 0;
    font-family: "Poiret One", sans-serif;
    font-weight: 400;
    color: var(--type);
  }
  .brand-name__main {
    top: 105px;
    text-align: center;
    font-size: 122px;
    line-height: 1;
    letter-spacing: 4px;
    text-transform: uppercase;
  }
  .brand-name__owner {
    top: 268px;
    right: 40px;
    left: auto;
    font-size: 46px;
    line-height: 1;
    text-align: right;
  }
</style>
</head>
<body>
  <main class="card">
    <div class="card__pattern" role="img" aria-label="Gold glitter zebra-stripe pattern with black stripes filling the card background"></div>
    <section class="brand-panel">
      <p class="brand-name brand-name__main">Velvette</p>
      <p class="brand-name brand-name__owner">by Monica Darsh</p>
    </section>
  </main>
</body>
</html>
```